Silver Bloom Marisol's Cleaning Service Business Cards Project

A business card with all contact details with logo design on there (already have a logo) eye catching Logo and contact info on one side, full logo on the back, must target upper class residential and corporate companies, fitness companies, still keep it on the feminine side of things , must look elegant

Target Market(s)

Upper class homes and corporate companies

Industry/Entity Type

Cleaning Service

Contact Information for Business Card

Name: Marisol Venturo
Position: Director
ABN: 47193802564
Email: marisolssilvercleaning@fernmail.test
Number: 0417968341

Font styles to use
Decorative

Colors

Designer to choose colors to be used in the design.

Requirements
Must have
• Available Sydney Wide, contact info and logo on one side, full logo on the back
Nice to have
• Professional appearance
Should not have
• Cheap advert looking stuff

```html
<!DOCTYPE html>
<html lang="en">
<head>
<meta charset="utf-8">
<title>Silver Bloom Business Cards</title>
<link rel="stylesheet" href="https://fonts.googleapis.com/css2?family=Cinzel:wght@600&family=Roboto:wght@400;500&display=swap">
<style>
  :root {
    --backdrop: #2a2a2c;
    --card: #1c1c1e;
    --card-edge: #262628;
    --silver: #d9d9dc;
    --silver-dim: #a9a9ad;
    --text: #f2f2f2;
    --accent: #4fc6cf;
  }
  * { margin: 0; padding: 0; box-sizing: border-box; }
  html, body {
    width: 1200px; height: 900px; overflow: hidden;
    background: var(--backdrop);
  }
  .canvas {
    position: relative; width: 1200px; height: 900px;
    display: flex; flex-direction: column; align-items: center; justify-content: center; gap: 56px;
  }
  .card {
    position: relative; width: 630px; height: 360px;
    background: linear-gradient(135deg, var(--card-edge), var(--card) 60%);
    border-radius: 4px;
  }
  .logo-lockup { display: flex; flex-direction: column; align-items: center; }
  .logo-mark { border-radius: 50%; background: var(--silver); }
  .ornament-area {
    border-radius: 12px;
    background: linear-gradient(90deg, rgba(217,217,220,0), rgba(217,217,220,0.35) 25%, rgba(217,217,220,0.35) 75%, rgba(217,217,220,0));
  }
  .brand {
    font-family: "Cinzel", serif; font-weight: 600; color: var(--silver);
    text-align: center; letter-spacing: 0.04em; line-height: 1.25;
  }
  .brand .brand-sub { display: block; letter-spacing: 0.3em; }

  /* back */
  .card-back { display: flex; align-items: center; justify-content: center; }
  .card-back .logo-mark { width: 78px; height: 78px; background: var(--silver-dim); }
  .card-back .ornament-area { width: 300px; height: 28px; margin: 8px 0 10px; }
  .card-back .brand { font-size: 38px; color: var(--silver-dim); }
  .card-back .brand-sub { font-size: 12px; margin-top: 6px; }

  /* front */
  .card-front .logo-block {
    position: absolute; left: 30px; top: 0; bottom: 0; width: 240px;
    display: flex; align-items: center; justify-content: center;
  }
  .card-front .logo-mark { width: 52px; height: 52px; }
  .card-front .ornament-area { width: 200px; height: 20px; margin: 6px 0 8px; }
  .card-front .brand { font-size: 25px; }
  .card-front .brand-sub { font-size: 7.5px; margin-top: 4px; }
  .divider {
    position: absolute; left: 290px; top: 75px; width: 2px; height: 210px; background: var(--text);
  }
  .contact {
    position: absolute; left: 318px; top: 80px; right: 20px;
    font-family: "Roboto", sans-serif; color: var(--text);
  }
  .contact-name { font-size: 28px; font-weight: 500; color: var(--accent); letter-spacing: 0.02em; white-space: nowrap; }
  .contact-role { font-size: 14px; margin-top: 2px; }
  .contact-list { list-style: none; margin-top: 18px; font-size: 15px; }
  .contact-list li { display: flex; align-items: center; gap: 9px; margin-top: 9px; white-space: nowrap; }
  .contact-list svg { width: 13px; height: 13px; flex: none; }
  .service-area { margin-top: 16px; font-size: 12px; letter-spacing: 0.18em; text-transform: uppercase; color: var(--silver-dim); }
</style>
</head>
<body>
<main class="canvas">
  <section class="card card-back">
    <div class="logo-lockup">
      <div class="logo-mark" role="img" aria-label="Silver Bloom mark"></div>
      <div class="ornament-area" role="img" aria-label="Silver floral flourish ornament"></div>
      <p class="brand">SILVER BLOOM<span class="brand-sub">MARISOL'S CLEANING SERVICE</span></p>
    </div>
  </section>

  <section class="card card-front">
    <div class="logo-block">
      <div class="logo-lockup">
        <div class="logo-mark" role="img" aria-label="Silver Bloom mark"></div>
        <div class="ornament-area" role="img" aria-label="Silver floral flourish ornament"></div>
        <p class="brand">SILVER BLOOM<span class="brand-sub">MARISOL'S CLEANING SERVICE</span></p>
      </div>
    </div>
    <div class="divider"></div>
    <div class="contact">
      <h1 class="contact-name">MARISOL VENTURO</h1>
      <p class="contact-role">Director</p>
      <ul class="contact-list">
        <li>ABN: 47193802564</li>
        <li>
          <svg viewBox="0 0 24 24" aria-hidden="true"><path fill="#4fc6cf" d="M6.6 10.8a15 15 0 0 0 6.6 6.6l2.2-2.2a1 1 0 0 1 1-.25 11.4 11.4 0 0 0 3.6.57 1 1 0 0 1 1 1V20a1 1 0 0 1-1 1A17 17 0 0 1 3 4a1 1 0 0 1 1-1h3.5a1 1 0 0 1 1 1c0 1.25.2 2.45.57 3.57a1 1 0 0 1-.25 1z"/></svg>
          0417968341
        </li>
        <li>
          <svg viewBox="0 0 24 24" aria-hidden="true"><rect x="2" y="5" width="20" height="14" rx="1.5" fill="none" stroke="#4fc6cf" stroke-width="2"/><path d="M2.5 6l9.5 7 9.5-7" fill="none" stroke="#4fc6cf" stroke-width="2"/></svg>
          marisolssilvercleaning@fernmail.test
        </li>
      </ul>
      <p class="service-area">Available Sydney Wide</p>
    </div>
  </section>
</main>
</body>
</html>
```